Wilderness Doc & TV personality personal page

I’m a wilderness and EMS emergency physician with particular sub specialties and a TV show. I need a website to highlight my interviews, teachings, etc... I did buy a number of domains for now.
Topics and things I need: CV (or version) me in the media, picture gallery, actually I sort of really like what dr ned harlow, my colleague has setup plus I have tv show and stuff like that. pinecrest rover dot com

Target Market(s)

EMS, education, commercial products...

Industry/Entity Type

Medical And Science

Coding

Coded - Design and coding required

Number of Pages Required

1 page

Font styles to use
Sans Serif

Colors
f37122
9bcb3c
0556a4
a54499

Requirements
Must have
• Links and photos to news articles and things that mention me that I can add in.
Nice to have
• Maybe some snapshots of lecture reviews or patient thank you notes. Accolades so to speak
• I really appreciate how sharp it is. I would love to see Headings that resemble my friend's at pinecrest rover dot com. Home, experience, consulting, lectures, affiliates, contact... those are main subjects... I think media also and that will have the TV show stuff and articles written about me...then maybe at the bottom of main page also have splits for training, research, television, and maybe exploration
Should not have
• The medical symbol with two snakes... that means quack doctor

```html
<!DOCTYPE html>
<html lang="en">
<head>
<meta charset="utf-8">
<title>Reviews, Blog and Contact</title>
<link href="https://fonts.googleapis.com/css2?family=Poppins:wght@400;500;600;700&family=Montserrat:wght@700&family=Raleway:ital,wght@0,300;0,400;1,300;1,400&display=swap" rel="stylesheet">
<style>
:root{
  --bg:#383838;
  --bg-dark:#323232;
  --card:#303030;
  --heading-box:#2e2e2e;
  --text:#ffffff;
  --muted:#a9a9a9;
  --line:#454545;
  --orange:#f37122;
  --green:#9bcb3c;
  --blue:#0556a4;
  --purple:#a54499;
}
*{margin:0;padding:0;box-sizing:border-box}
html,body{width:1200px;height:2841px;overflow:hidden;background:var(--bg)}
body{position:relative;font-family:"Raleway",sans-serif;color:var(--text)}
.abs{position:absolute}
.section-title{position:absolute;left:0;width:1200px;text-align:center;font-family:"Poppins",sans-serif;font-weight:500;font-size:21px;letter-spacing:.6px;line-height:1}
.title-box{position:absolute;background:var(--heading-box)}
.photo{position:absolute}
.review-text{position:absolute;width:215px}
.review-text h3{font-family:"Poppins",sans-serif;font-weight:500;font-size:13.5px;letter-spacing:.3px;margin-bottom:10px}
.review-text .by{font-size:8.5px;font-style:italic;margin-bottom:9px}
.review-text p{font-size:10px;line-height:22.5px;color:var(--muted);font-weight:300}
.review-text .read{position:absolute;top:212px;font-family:"Poppins",sans-serif;font-size:8.5px;font-weight:600;color:var(--blue);letter-spacing:.3px}
.divider{position:absolute;left:161px;top:718px;width:878px;height:1px;background:var(--line)}
.testi{position:absolute;top:808px;width:278px;height:208px;background:var(--card);text-align:center}
.avatar{position:absolute;left:30px;top:-30px;width:60px;height:60px;border-radius:50%;background:linear-gradient(#9a8a80,#5c514b);border:2px solid #ddd}
.testi h4{margin-top:27px;font-family:"Poppins",sans-serif;font-weight:500;font-size:13px}
.testi .role{margin-top:6px;font-size:10px;font-style:italic;color:var(--muted)}
.testi svg{display:block;margin:11px auto 0}
.testi p{margin-top:14px;font-size:10px;font-style:italic;line-height:23px;color:var(--muted);padding:0 28px;text-align:left}
.dots span{position:absolute;top:1063px;width:10px;height:10px;border-radius:50%;background:#666}
.dots span.on{width:14px;height:14px;top:1061px;background:#fff}
.stats{position:absolute;left:0;top:1136px;width:1200px;height:268px;background:linear-gradient(90deg,#2c2c2c,#3b3736 30%,#35302f 60%,#2a2a2a)}
.stat{position:absolute;top:1196px;width:240px;text-align:center}
.stat .num{font-family:"Montserrat",sans-serif;font-weight:700;font-size:54px;letter-spacing:3px;line-height:1.2}
.stat .bar{width:38px;height:2px;margin:23px auto 0}
.stat .label{margin-top:27px;font-size:15px;font-style:italic;font-weight:300;color:#bdbdbd}
.post{position:absolute;top:1551px;width:278px;height:521px;background:var(--card)}
.post .photo{left:0;top:0;width:278px;height:314px}
.post h3{position:absolute;left:23px;top:340px;font-family:"Poppins",sans-serif;font-weight:500;font-size:14px;letter-spacing:.3px}
.post .meta{position:absolute;left:23px;top:366px;font-size:8.5px;font-style:italic;color:var(--muted)}
.post .meta span{margin-right:14px}
.post p{position:absolute;left:23px;top:393px;width:240px;font-size:10px;font-style:italic;line-height:23px;color:var(--muted)}
.post .more{position:absolute;right:23px;top:483px;font-family:"Poppins",sans-serif;font-size:9.5px;font-weight:600}
.video-cue{position:absolute;left:0;width:278px;text-align:center;font-family:"Poppins",sans-serif}
.video-cue b{display:block;font-size:9.5px;font-weight:700;line-height:15px}
.video-cue u{display:block;margin-top:3px;font-size:9.5px;font-style:italic;font-family:"Raleway",sans-serif}
.btn{position:absolute;left:543px;width:113px;height:45px;background:var(--blue);color:#fff;font-family:"Poppins",sans-serif;font-weight:600;font-size:9px;display:flex;align-items:center;justify-content:center;letter-spacing:.2px}
.contact-bg{position:absolute;left:0;top:2226px;width:1200px;height:615px;background:var(--bg-dark)}
.field{position:absolute;border:1px solid #4a4a4a;font-size:9.5px;font-style:italic;color:#8f8f8f;padding:0 11px;display:flex;align-items:center}
.field.area{align-items:flex-start;padding-top:12px}
</style>
</head>
<body>

<!-- Reviews -->
<div class="title-box" style="left:469px;top:52px;width:82px;height:43px"></div>
<h2 class="section-title" style="top:64px">Reviews &amp; Testimonials</h2>

<div class="photo" role="img" aria-label="Rescuer in red suit abseiling a grey rock face" style="left:161px;top:140px;width:203px;height:247px;background:linear-gradient(135deg,#8a8a88,#5f605e 55%,#7a7a78)"></div>
<div class="review-text" style="left:385px;top:153px">
  <h3>Lorem Ipsum Dolor</h3><div class="by">By: Lorem Ipsum</div>
  <p>Lorem ipsum dolor amet tilde etsy pork belly cray mixtape. Scenester swag viral raw denim kale chips plaid trust fund quinoa migas small batch master cleanse you proba-bly haven't heard of them. Echo park quinoa hexagon brunch. Trust fund flexitarian paleo</p>
  <span class="read">READ THE REVIEW &gt;&gt;</span>
</div>

<div class="photo" role="img" aria-label="Paramedic wheeling a stretcher beside an ambulance" style="left:611px;top:140px;width:203px;height:247px;background:linear-gradient(90deg,#3f4a3a,#5b5f55 45%,#d8d8d2 60%,#e6e6e0)"></div>
<div class="review-text" style="left:835px;top:153px">
  <h3>Lorem Ipsum Dolor</h3><div class="by">By: Lorem Ipsum</div>
  <p>Lorem ipsum dolor amet tilde etsy pork belly cray mixtape. Scenester swag viral raw denim kale chips plaid trust fund quinoa migas small batch master cleanse you proba-bly haven't heard of them. Echo park quinoa hexagon brunch. Trust fund flexitarian paleo</p>
  <span class="read">READ THE REVIEW &gt;&gt;</span>
</div>

<div class="photo" role="img" aria-label="Emergency team in blue shirts posing in front of ambulances" style="left:161px;top:410px;width:203px;height:247px;background:linear-gradient(180deg,#c9d3dc,#aab8c4 30%,#3f6fae 55%,#26344a)"></div>
<div class="review-text" style="left:385px;top:423px">
  <h3>Lorem Ipsum Dolor</h3><div class="by">By: Lorem Ipsum</div>
  <p>Lorem ipsum dolor amet tilde etsy pork belly cray mixtape. Scenester swag viral raw denim kale chips plaid trust fund quinoa migas small batch master cleanse you proba-bly haven't heard of them. Echo park quinoa hexagon brunch. Trust fund flexitarian paleo</p>
  <span class="read">READ THE REVIEW &gt;&gt;</span>
</div>

<div class="photo" role="img" aria-label="Firefighter pointing through smoke" style="left:611px;top:410px;width:203px;height:247px;background:linear-gradient(135deg,#6d6f6e,#4a4a48 50%,#2a2a26)"></div>
<div class="review-text" style="left:835px;top:423px">
  <h3>Lorem Ipsum Dolor</h3><div class="by">By: Lorem Ipsum</div>
  <p>Lorem ipsum dolor amet tilde etsy pork belly cray mixtape. Scenester swag viral raw denim kale chips plaid trust fund quinoa migas small batch master cleanse you proba-bly haven't heard of them. Echo park quinoa hexagon brunch. Trust fund flexitarian paleo</p>
  <span class="read">READ THE REVIEW &gt;&gt;</span>
</div>

<div class="divider"></div>

<!-- Patient testimonials -->
<div class="testi" style="left:161px">
  <div class="avatar" role="img" aria-label="Portrait of Jason Callow"></div>
  <h4>Jason Callow</h4><div class="role">Patient</div>
  <svg width="30" height="24" viewBox="0 0 30 24" fill="var(--orange)"><path d="M2 2h10v10c0 6-4 10-10 11v-4c3-1 5-3 5-6H2z"/><path d="M17 2h10v10c0 6-4 10-10 11v-4c3-1 5-3 5-6h-5z"/></svg>
  <p>Trust fund flexitarian paleo before they sold out. Hexagon portland sustainable, aesthetic and if a leggings prism synth polaroid. VHS pour- ramps</p>
</div>
<div class="testi" style="left:461px">
  <div class="avatar" role="img" aria-label="Portrait of Marta Kerrin"></div>
  <h4>Marta Kerrin</h4><div class="role">Patient</div>
  <svg width="30" height="24" viewBox="0 0 30 24" fill="var(--green)"><path d="M2 2h10v10c0 6-4 10-10 11v-4c3-1 5-3 5-6H2z"/><path d="M17 2h10v10c0 6-4 10-10 11v-4c3-1 5-3 5-6h-5z"/></svg>
  <p>Trust fund flexitarian paleo before they sold out. Hexagon portland sustainable, aesthetic and if a leggings prism synth polaroid. VHS pour- ramps</p>
</div>
<div class="testi" style="left:761px">
  <div class="avatar" role="img" aria-label="Portrait of Andy Walsh"></div>
  <h4>Andy Walsh</h4><div class="role">Patient</div>
  <svg width="30" height="24" viewBox="0 0 30 24" fill="var(--purple)"><path d="M2 2h10v10c0 6-4 10-10 11v-4c3-1 5-3 5-6H2z"/><path d="M17 2h10v10c0 6-4 10-10 11v-4c3-1 5-3 5-6h-5z"/></svg>
  <p>Trust fund flexitarian paleo before they sold out. Hexagon portland sustainable, aesthetic and if a leggings prism synth polaroid. VHS pour- ramps</p>
</div>
<div class="dots"><span style="left:570px"></span><span class="on" style="left:592px"></span><span style="left:618px"></span></div>

<!-- Stats -->
<div class="stats" role="img" aria-label="Darkened street scene with fire trucks and crowd"></div>
<div class="stat" style="left:142px"><div class="num">150</div><div class="bar" style="background:var(--orange)"></div><div class="label">Emergency Medical Services</div></div>
<div class="stat" style="left:369px"><div class="num">100</div><div class="bar" style="background:var(--green)"></div><div class="label">Patients Cured</div></div>
<div class="stat" style="left:591px"><div class="num">120</div><div class="bar" style="background:var(--blue)"></div><div class="label">TV Interviews</div></div>
<div class="stat" style="left:836px"><div class="num">70</div><div class="bar" style="background:var(--purple)"></div><div class="label">Emergent Cases Solved</div></div>

<!-- Blog -->
<div class="title-box" style="left:496px;top:1457px;width:83px;height:43px"></div>
<h2 class="section-title" style="top:1468px">Recent Blog Posts</h2>

<div class="post" style="left:161px">
  <div class="photo" role="img" aria-label="Fire truck glowing red at night with a firefighter" style="background:linear-gradient(135deg,#e0242a,#8c0a0e 55%,#2a0405)"></div>
  <h3>Emergent Service Of Lorem</h3>
  <div class="meta"><span>By: Admin</span>Posted: 19/12/2018</div>
  <p>Excepteur sint occaecat cupidatat non proident, sunt in culpa qui officia deserunt mollit anim id est laborum. Sed ut perspiciatis unde omnis iste natus</p>
  <span class="more">READ MORE</span>
</div>
<div class="post" style="left:461px">
  <div class="photo" role="img" aria-label="Weathered emergency door with a window onto trees" style="background:linear-gradient(180deg,#4c6272,#6f8797 40%,#8aa36c 60%,#6f8797)"></div>
  <h3>Emergent Service Of Lorem</h3>
  <div class="meta"><span>By: Admin</span>Posted: 19/12/2018</div>
  <p>Excepteur sint occaecat cupidatat non proident, sunt in culpa qui officia deserunt mollit anim id est laborum. Sed ut perspiciatis unde omnis iste natus</p>
  <span class="more" style="color:var(--blue)">READ MORE</span>
</div>
<div class="post" style="left:761px">
  <div class="photo" role="img" aria-label="Firefighter by a burning vehicle, video still" style="background:linear-gradient(135deg,#6b5f56,#8a7a6c 40%,#55524e)"></div>
  <svg class="abs" style="left:126px;top:113px" width="30" height="34" viewBox="0 0 30 34"><path d="M0 0L30 17L0 34z" fill="var(--blue)"/></svg>
  <div class="video-cue" style="top:157px"><b>Click The Link Below<br>To Watch The Video</b><u>www.vidhaven.tv/4334fds0asd</u></div>
  <h3>Rare Emergency Video</h3>
  <div class="meta"><span>By: Admin</span>Posted: 19/12/2018</div>
  <p>Excepteur sint occaecat cupidatat non proident, sunt in culpa qui officia deserunt mollit anim id est laborum. Sed ut perspiciatis unde omnis iste natus</p>
  <span class="more">READ MORE</span>
</div>

<a class="btn" style="top:2119px">VIEW ALL</a>

<!-- Contact -->
<div class="contact-bg"></div>
<div class="title-box" style="left:491px;top:2287px;width:83px;height:43px"></div>
<h2 class="section-title" style="top:2298px">Let's Keep In Touch</h2>

<div class="field" style="left:312px;top:2389px;width:276px;height:29px">Your Name Here*</div>
<div class="field" style="left:611px;top:2389px;width:277px;height:29px">Your E-mail Address Here*</div>
<div class="field" style="left:312px;top:2434px;width:276px;height:29px">Your Phone Number Here*</div>
<div class="field" style="left:611px;top:2434px;width:277px;height:29px">Subject*</div>
<div class="field area" style="left:312px;top:2486px;width:576px;height:178px">Your Message Here...</div>

<a class="btn" style="top:2696px">SEND MESSAGE</a>

</body>
</html>
```